New Business Card for Web Design/Internet Marketing Company

Looking for a great looking new business card. We are a 10 year old web design, internet marketing and website management company that works mostly with small businesses.

Our new card needs to better match the colors and style of our website, be bold, extremely usable and slightly edgy.

Target Market(s)

Small/Medium businesses that have websites

Industry/Entity Type

Internet

Requirements
Must have
• Front and back design, full color, rounded corners please

Must use the colors/style of our website (JPG provided)

INFO FOR CARDS (as readable as possible please)
Mark Pellow
President/CEO
mark@brightlanesites.com
Phone: 520-481-7093
Toll Free: 866-481-7093
Address: 4315 E. Kestrel Ave. Ste. 140, Tucson, AZ 85733

THINGS I WANT TO PROMOTE (if there is room):
1. Our Website - www.brightlanesites.com

2. Social Media
Twitter: @brightlanesites
Facebook: www.facebook.com/brightlanesites

3. Our Services
Web Design
Internet Marketing
Website Management

```html
<!DOCTYPE html>
<html lang="en">
<head>
<meta charset="utf-8">
<title>Brightlane Sites – Business Card</title>
<link href="https://fonts.googleapis.com/css2?family=Lato:wght@400;700;900&display=swap" rel="stylesheet">
<style>
  :root {
    --canvas: #e9ebee;
    --white: #ffffff;
    --paper-shade: #eceef0;
    --navy: #0f3768;
    --navy-deep: #0a2547;
    --sky: #4fc0ec;
    --sky-light: #8ad6f4;
    --brand-blue: #1a8ac6;
    --orange: #ee7d24;
    --ink: #5a5d61;
    --ink-dark: #444;
  }
  * { margin: 0; padding: 0; box-sizing: border-box; }
  html, body {
    width: 1200px; height: 900px; overflow: hidden;
    background: var(--canvas);
    font-family: "Lato", sans-serif;
  }
  .card {
    position: absolute;
    width: 620px; height: 354px;
    border-radius: 26px;
    overflow: hidden;
    box-shadow: 0 10px 28px rgba(0,0,0,.18);
  }
  .card-front { left: 60px; top: 60px; background: linear-gradient(135deg, var(--white) 40%, var(--paper-shade)); }
  .card-back { left: 520px; top: 486px; background: radial-gradient(ellipse at 45% 40%, #1a4d8a, var(--navy) 55%, var(--navy-deep)); }
  .band { position: absolute; inset: 0; width: 100%; height: 100%; }
  .brand {
    position: absolute; display: flex; align-items: center; gap: 12px;
    font-weight: 900; color: var(--brand-blue); letter-spacing: -0.5px; line-height: 1;
  }
  .brand-dot { border-radius: 50%; background: var(--orange); flex: none; }
  .card-front .brand { left: 40px; top: 92px; font-size: 38px; }
  .card-front .brand-dot { width: 34px; height: 34px; }
  .card-back .brand { left: 0; right: 0; top: 108px; justify-content: center; font-size: 56px; }
  .card-back .brand-dot { width: 50px; height: 50px; }
  .social { position: absolute; right: 34px; top: 30px; list-style: none; }
  .social li { display: flex; align-items: center; gap: 10px; font-size: 18px; color: var(--ink); margin-bottom: 12px; }
  .social-mark { width: 20px; height: 20px; border-radius: 3px; background: var(--brand-blue); }
  .person { position: absolute; left: 40px; top: 162px; font-size: 26px; line-height: 32px; color: var(--ink); }
  .person .role { font-size: 22px; letter-spacing: .5px; }
  .contacts { position: absolute; left: 40px; top: 222px; list-style: none; }
  .contacts li { display: flex; align-items: center; gap: 10px; font-size: 17px; color: var(--ink-dark); line-height: 22px; }
  .contacts svg { width: 16px; height: 16px; flex: none; }
  .address { position: absolute; left: 364px; top: 204px; font-size: 17px; line-height: 23px; color: var(--ink); font-style: normal; }
  .services { position: absolute; left: 0; right: 0; top: 196px; text-align: center; font-size: 19px; color: var(--white); letter-spacing: .3px; }
  .services span { margin: 0 10px; opacity: .8; }
  .website { position: absolute; left: 0; right: 0; top: 300px; text-align: center; font-size: 22px; font-weight: 900; color: var(--navy); }
</style>
</head>
<body>

<section class="card card-front" aria-label="Card front">
  <svg class="band" viewBox="0 0 620 354" preserveAspectRatio="none" aria-hidden="true">
    <defs>
      <linearGradient id="skyFront" x1="0" y1="0" x2="0" y2="1">
        <stop offset="0" stop-color="#8ad6f4"/><stop offset="1" stop-color="#3fb7e8"/>
      </linearGradient>
    </defs>
    <path d="M0 330 Q 330 315 620 250 L620 354 L0 354 Z" fill="url(#skyFront)"/>
    <path d="M0 330 Q 330 315 620 250" fill="none" stroke="#ee7d24" stroke-width="4"/>
  </svg>

  <ul class="social">
    <li><span class="social-mark"></span>@brightlanesites</li>
    <li><span class="social-mark"></span>/brightlanesites</li>
  </ul>

  <div class="brand"><span class="brand-dot"></span>Brightlane Sites</div>

  <p class="person">Mark Pellow <span class="role">| PRESIDENT / CEO</span></p>

  <ul class="contacts">
    <li>
      <svg viewBox="0 0 16 16"><rect x="1" y="2" width="14" height="12" rx="1.5" fill="none" stroke="#ee7d24" stroke-width="1.5"/><rect x="4" y="5" width="4" height="6" fill="#ee7d24"/><circle cx="11" cy="6" r="1" fill="#ee7d24"/><circle cx="11" cy="10" r="1" fill="#ee7d24"/></svg>
      520-481-7093
    </li>
    <li>
      <svg viewBox="0 0 16 16"><rect x="4" y="1" width="8" height="14" rx="1.5" fill="none" stroke="#ee7d24" stroke-width="1.5"/><rect x="6" y="3.5" width="4" height="5" fill="#ee7d24"/></svg>
      866-481-7093 free
    </li>
    <li>
      <svg viewBox="0 0 16 16"><rect x="1" y="3" width="14" height="10" fill="none" stroke="#ee7d24" stroke-width="1.5"/><path d="M1 3 L8 9 L15 3 M1 13 L6 8 M15 13 L10 8" fill="none" stroke="#ee7d24" stroke-width="1.3"/></svg>
      mark@brightlanesites.com
    </li>
  </ul>

  <address class="address">4315 E. Kestrel Ave. Ste. 140,<br>Tucson, AZ 85733</address>
</section>

<section class="card card-back" aria-label="Card back">
  <svg class="band" viewBox="0 0 620 354" preserveAspectRatio="none" aria-hidden="true">
    <defs>
      <linearGradient id="skyBack" x1="0" y1="0" x2="0" y2="1">
        <stop offset="0" stop-color="#8ad6f4"/><stop offset="1" stop-color="#4fc0ec"/>
      </linearGradient>
    </defs>
    <path d="M0 282 Q 320 262 620 232 L620 354 L0 354 Z" fill="url(#skyBack)"/>
    <path d="M0 282 Q 320 262 620 232" fill="none" stroke="#ee7d24" stroke-width="5"/>
  </svg>

  <div class="brand"><span class="brand-dot"></span>Brightlane Sites</div>

  <p class="services">Web Design<span>|</span>Internet Marketing<span>|</span>Website Management</p>

  <p class="website">www.brightlanesites.com</p>
</section>

</body>
</html>
```